Event Space Website (clone)

the name of the company is KINDLYHOST.com
i’ll have a logo shortly

i basically need a clone of the following website
https://ashlarrooms.example/
i would really like the design to be with stock photos
and then after choosing the winner i will supply my photos
(im doing some all new photo shoots this week)

id love the designer to put their OWN spin on this site

Target Market(s)

nyc urban market

Industry/Entity Type

Event Planning

Coding

Coded - Design and coding required

Number of Pages Required

1 page

Font styles to use
Serif

Requirements
Must have
• from top to bottom ill just list what i need copied

LOCATIONS FAQ CONTACT AND SOCIAL MEDIA LINKS NEED

i need the slider ... for sure

please change classics to current locations
please show
Harlem
Brooklyn
Bronx (for bronx show an image of coming soon)

please change events with a view to
Harlem Venues
1. Kindly Ashgrove
2. Kindly Upper Ashgrove

please change Our biggest and boldest to Brooklyn Venues
1. Kindly Fernwick
2. Kindly Holloway (1)
3. Kindly holloway (2)
4. Kindly Holloway rooftop

remove latest ventures
remove asian couple kissing

keep interested in this location
keep why chose us

keep contact us area
keep social media plug in
Nice to have
• ur own flair and style

PLEASE dont forget that all the individual sections
example
kindly ashgrove
kindly upper ashgrove
will have their own individual micro pages .... that will be placed under brooklyn venues (ive attached an example for clarity)

```html
<!DOCTYPE html>
<html lang="en">
<head>
<meta charset="utf-8">
<title>KINDLYHOST — Event Spaces</title>
<link rel="stylesheet" href="https://fonts.googleapis.com/css2?family=Cinzel:wght@400;500;600&family=Open+Sans:wght@400;600&family=Roboto:wght@400;500&display=swap">
<style>
:root{
  --red:#e5173e;
  --red-band:#d9365c;
  --ink:#222222;
  --muted:#8a8a8a;
  --line:#d9d9d9;
  --panel:#f6f6f6;
  --dark:#1c150f;
  --white:#ffffff;
}
*{box-sizing:border-box;margin:0;padding:0}
html,body{width:1200px;height:5172px;overflow:hidden;background:var(--white)}
body{font-family:"Open Sans",sans-serif;color:var(--ink);position:relative}
.abs{position:absolute}
.serif{font-family:"Cinzel",serif;font-weight:500}
.photo{position:absolute;display:block}

/* hero */
.hero{left:0;top:0;width:1200px;height:740px}
.hero-shape{position:absolute;inset:0}
.nav{left:110px;top:30px;width:980px;height:40px;display:flex;align-items:center;color:var(--white)}
.brand{font-family:"Cinzel",serif;font-size:27px;font-weight:500;letter-spacing:1px;color:var(--white)}
.nav-links{margin-left:auto;display:flex;gap:34px;font-size:15px;letter-spacing:.5px;text-transform:uppercase}
.socials{display:flex;gap:10px;margin-left:38px}
.social{width:40px;height:40px;border:2px solid currentColor;border-radius:50%}
.hero-title{left:0;top:140px;width:1200px;text-align:center;font-family:"Cinzel",serif;font-size:80px;color:var(--white);letter-spacing:2px}
.hero-sub{left:0;top:240px;width:1200px;text-align:center;font-size:25px;font-weight:600;color:var(--white)}
.btn{display:block;background:var(--red);color:var(--white);text-align:center;border-radius:30px;font-weight:600;text-transform:uppercase}
.hero-btn{left:489px;top:293px;width:222px;height:58px;line-height:58px;font-size:18px}
.dots{left:534px;top:582px;display:flex;gap:5px}
.dots span{width:30px;height:5px;background:rgba(255,255,255,.6)}
.dots span:first-child{background:var(--white)}

.h2{position:absolute;left:0;width:1200px;text-align:center;font-family:"Cinzel",serif;font-size:42px;font-weight:500;color:var(--ink);letter-spacing:1px}
.label{position:absolute;text-align:center;font-size:19px;color:var(--ink);text-transform:uppercase;letter-spacing:.5px}

/* harlem */
.harlem-bg{left:0;top:1366px;width:1200px;height:502px}
.harlem-title{left:110px;top:1548px;font-family:"Cinzel",serif;font-size:42px;line-height:60px}

/* steps */
.steps-bg{left:0;top:2696px;width:1200px;height:610px}
.steps-title{position:absolute;left:0;top:2796px;width:1200px;text-align:center;font-family:"Cinzel",serif;font-size:42px;line-height:52px;color:var(--white)}
.step{position:absolute;top:2926px;width:240px;text-align:center;color:var(--white)}
.step-circle{width:168px;height:168px;border-radius:50%;background:var(--white);margin:0 auto;display:flex;align-items:center;justify-content:center}
.step-name{margin-top:22px;font-size:20px;line-height:25px;text-transform:uppercase}

/* why */
.why{position:absolute;width:320px;height:100px}
.why svg{position:absolute;left:0;top:0}
.why h3{position:absolute;left:112px;top:0;font-family:"Roboto",sans-serif;font-weight:400;font-size:20px;text-transform:uppercase;letter-spacing:.5px}
.why p{position:absolute;left:112px;top:34px;width:200px;font-family:"Cinzel",serif;font-family:Georgia,serif;font-size:15px;line-height:22px;color:var(--muted)}

/* form */
.form-bg{left:0;top:3760px;width:1200px;height:890px}
.form-title{top:3905px;color:var(--white)}
.field-label{position:absolute;font-family:"Roboto",sans-serif;font-size:15px;font-weight:500;color:var(--white);text-transform:uppercase}
.input{position:absolute;background:var(--white);height:42px}
.check{position:absolute;font-family:"Roboto",sans-serif;font-size:15px;color:var(--white);display:flex;align-items:center;gap:9px;white-space:nowrap}
.check i{width:14px;height:14px;border:2px solid var(--white);border-radius:2px;display:block}
.submit{left:529px;top:4502px;width:142px;height:58px;line-height:58px;font-size:17px}

/* footer */
.foot-brand{left:110px;top:4712px;font-family:"Cinzel",serif;font-size:50px;letter-spacing:1px}
.foot-item{position:absolute;left:110px;display:flex;gap:12px;font-size:15px;line-height:21px;color:#555}
.foot-item svg{flex:none;margin-top:2px}
.quick{left:495px;top:4718px;font-family:"Roboto",sans-serif}
.quick h4{font-weight:500;font-size:17px;margin-bottom:14px}
.quick a{display:block;font-size:15px;color:#555;text-decoration:none;line-height:32px}
.thumb{position:absolute;width:135px;height:102px}
.rule{left:110px;top:5094px;width:980px;height:1px;background:var(--line)}
.copy{left:110px;top:5128px;font-size:15px;color:#444}
.foot-socials{left:942px;top:5115px;display:flex;gap:10px;color:var(--red)}
</style>
</head>
<body>

<!-- HERO -->
<header class="abs hero">
  <svg class="hero-shape" width="1200" height="740" viewBox="0 0 1200 740" role="img" aria-label="Slider photo of a dimly lit banquet hall filled with guests at a party">
    <defs>
      <linearGradient id="heroFill" x1="0" y1="0" x2="1" y2="1">
        <stop offset="0" stop-color="#6b4518"/>
        <stop offset=".45" stop-color="#3a2412"/>
        <stop offset="1" stop-color="#1a120c"/>
      </linearGradient>
    </defs>
    <polygon points="0,0 1200,0 1200,606 600,738 0,606" fill="url(#heroFill)"/>
  </svg>
  <nav class="abs nav">
    <span class="brand">KINDLYHOST</span>
    <div class="nav-links"><span>Locations</span><span>FAQ</span><span>Contact</span></div>
    <div class="socials"><span class="social" aria-label="Social link"></span><span class="social" aria-label="Social link"></span><span class="social" aria-label="Social link"></span></div>
  </nav>
  <h1 class="abs hero-title">KINDLYHOST</h1>
  <p class="abs hero-sub">Lorem ipsum dolor sit ame onsect</p>
  <span class="abs btn hero-btn">Get more info</span>
  <div class="abs dots"><span></span><span></span><span></span><span></span></div>
</header>

<!-- CURRENT LOCATIONS -->
<h2 class="h2" style="top:806px">Current Locations</h2>
<div class="photo" style="left:110px;top:900px;width:310px;height:342px;background:linear-gradient(160deg,#8fc3ec 0%,#c9a27a 45%,#8a4a30 100%)" role="img" aria-label="Aerial photo of Harlem streets and buildings"></div>
<div class="photo" style="left:444px;top:900px;width:310px;height:342px;background:linear-gradient(180deg,#d9b07a 0%,#9c7a55 45%,#4f6a6a 100%)" role="img" aria-label="Photo of the Brooklyn Bridge at sunset"></div>
<div class="photo" style="left:778px;top:900px;width:310px;height:342px;background:radial-gradient(circle at 50% 45%,#d41a22 0%,#8a0a10 60%,#3b0305 100%)" role="img" aria-label="Red stage curtain with coming soon lettering"></div>
<p class="label" style="left:110px;top:1260px;width:310px">Harlem</p>
<p class="label" style="left:444px;top:1260px;width:310px">Brooklyn</p>
<p class="label" style="left:778px;top:1260px;width:310px">Bronx</p>

<!-- HARLEM VENUES -->
<svg class="abs harlem-bg" width="1200" height="502" viewBox="0 0 1200 502"><polygon points="0,62 600,0 1200,62 1200,502 0,502" fill="var(--panel)"/></svg>
<h2 class="abs harlem-title">Harlem<br>Venues</h2>
<div class="photo" style="left:354px;top:1456px;width:356px;height:320px;background:linear-gradient(180deg,#b8664a 0%,#e8b49a 40%,#6b2a1c 100%)" role="img" aria-label="Kindly Ashgrove auditorium with stage and rows of seats"></div>
<div class="photo" style="left:734px;top:1456px;width:356px;height:320px;background:linear-gradient(180deg,#9fd6c0 0%,#6a7a78 45%,#8d8f92 100%)" role="img" aria-label="Kindly Upper Ashgrove banquet room with round tables"></div>
<p class="label" style="left:354px;top:1788px;width:356px">Kindly Ashgrove</p>
<p class="label" style="left:734px;top:1788px;width:356px">Kindly Upper Ashgrove</p>

<!-- BROOKLYN VENUES -->
<h2 class="h2" style="top:1920px">Brooklyn Venues</h2>
<div class="photo" style="left:110px;top:2020px;width:478px;height:262px;background:linear-gradient(180deg,#cfd6e0 0%,#a79a88 50%,#5e5a58 100%)" role="img" aria-label="Kindly Fernwick ballroom with decorated ceiling and round tables"></div>
<div class="photo" style="left:612px;top:2020px;width:478px;height:262px;background:linear-gradient(180deg,#2aa8a0 0%,#2e4f78 35%,#4d4d4f 100%)" role="img" aria-label="Kindly Holloway (1) event hall with blue and green lighting"></div>
<div class="photo" style="left:110px;top:2350px;width:478px;height:262px;background:linear-gradient(180deg,#e7e7e4 0%,#b9b3a9 55%,#5e5856 100%)" role="img" aria-label="Kindly Holloway (2) open workspace with desks and pendant lamps"></div>
<div class="photo" style="left:612px;top:2350px;width:478px;height:262px;background:linear-gradient(180deg,#dfe4ea 0%,#9a8e84 35%,#e5e3df 100%)" role="img" aria-label="Kindly Holloway rooftop terrace with lounge chairs and city skyline"></div>
<p class="label" style="left:110px;top:2296px;width:478px">Kindly Fernwick</p>
<p class="label" style="left:612px;top:2296px;width:478px">Kindly Holloway (1)</p>
<p class="label" style="left:110px;top:2626px;width:478px">Kindly Holloway (2)</p>
<p class="label" style="left:612px;top:2626px;width:478px">Kindly Holloway rooftop</p>

<!-- STEPS -->
<svg class="abs steps-bg" width="1200" height="610" viewBox="0 0 1200 610" role="img" aria-label="Event hall photo under a red tint">
  <polygon points="0,86 600,0 1200,86 1200,506 600,610 0,506" fill="var(--red-band)"/>
  <polygon points="0,86 600,0 1200,86 1200,150 0,150" fill="#b8203f" opacity=".5"/>
</svg>
<h2 class="steps-title">Interested in locking<br>in a location?</h2>
<svg class="abs" style="left:0;top:3000px" width="1200" height="24" viewBox="0 0 1200 24" fill="none" stroke="#fff" stroke-width="2">
  <path d="M318 12h44M354 5l8 7-8 7"/><path d="M562 12h46M600 5l8 7-8 7"/><path d="M808 12h46M846 5l8 7-8 7"/>
</svg>
<div class="step" style="left:110px">
  <div class="step-circle"><svg width="130" height="70" viewBox="0 0 130 70" fill="none" stroke="#222" stroke-width="4"><path d="M4 22h30M10 34h24M16 46h18"/><rect x="40" y="8" width="84" height="54" transform="rotate(-4 82 35)"/><path d="M42 12l40 28 40-32" /></svg></div>
  <p class="step-name">Send us a<br>note</p>
</div>
<div class="step" style="left:356px">
  <div class="step-circle"><svg width="90" height="100" viewBox="0 0 90 100" fill="none" stroke="#222" stroke-width="4"><path d="M38 92C20 66 8 52 8 36a30 30 0 0 1 60 0c0 8-3 16-8 24"/><circle cx="38" cy="36" r="12"/><circle cx="64" cy="72" r="18" stroke="var(--red)"/><path d="M55 72l7 7 12-14" stroke="#222"/></svg></div>
  <p class="step-name">Check out the<br>location</p>
</div>
<div class="step" style="left:602px">
  <div class="step-circle"><svg width="96" height="96" viewBox="0 0 96 96" fill="none" stroke="#222" stroke-width="4"><rect x="6" y="14" width="84" height="76"/><path d="M6 30h84M20 6v16M36 6v16M52 6v16M68 6v16M80 6v16"/><path d="M32 58l12 12 22-22"/></svg></div>
  <p class="step-name">Pick your<br>perfect date</p>
</div>
<div class="step" style="left:848px">
  <div class="step-circle"><svg width="110" height="104" viewBox="0 0 110 104" fill="none" stroke="#222" stroke-width="4"><rect x="34" y="6" width="50" height="32" rx="10"/><path d="M52 38l-6 10 14-10"/><circle cx="48" cy="22" r="3"/><circle cx="59" cy="22" r="3"/><circle cx="70" cy="22" r="3"/><circle cx="30" cy="54" r="14"/><path d="M8 100c0-20 10-30 22-30s22 10 22 30"/><circle cx="80" cy="54" r="14"/><path d="M58 100c0-20 10-30 22-30s22 10 22 30"/></svg></div>
  <p class="step-name">Plan</p>
</div>

<!-- WHY CHOOSE US -->
<h2 class="h2" style="top:3362px">Why choose us?</h2>
<div class="why" style="left:120px;top:3466px">
  <svg width="90" height="90" viewBox="0 0 90 90" fill="none" stroke="#222" stroke-width="3"><circle cx="45" cy="45" r="26"/><path d="M45 8v10M45 72v10M8 45h10M72 45h10M19 19l7 7M64 64l7 7M71 19l-7 7M26 64l-7 7"/><path d="M34 45l8 8 22-22" stroke="var(--red)"/></svg>
  <h3>Customizable</h3><p>Nemo enim ipsam volup tatem quia ptsit.</p>
</div>
<div class="why" style="left:452px;top:3466px">
  <svg width="90" height="90" viewBox="0 0 90 90" fill="none" stroke="#222" stroke-width="3"><rect x="14" y="8" width="70" height="50"/><rect x="4" y="40" width="24" height="42" rx="3"/><path d="M34 48l40-30" stroke="var(--red)"/><path d="M66 18h8v8" stroke="var(--red)"/></svg>
  <h3>Responsive</h3><p>Nemo enim ipsam volup tatem quia ptsit.</p>
</div>
<div class="why" style="left:786px;top:3466px">
  <svg width="90" height="90" viewBox="0 0 90 90" fill="none" stroke="#222" stroke-width="3"><circle cx="50" cy="22" r="18" stroke="var(--red)"/><path d="M42 22l6 6 12-12" stroke="var(--red)"/><rect x="4" y="52" width="12" height="28"/><path d="M16 58h22l14 6h-16M16 76h30l36-18c-4-4-10-4-14 0"/></svg>
  <h3>Easy</h3><p>Nemo enim ipsam volup tatem quia ptsit.</p>
</div>
<div class="why" style="left:286px;top:3616px">
  <svg width="100" height="100" viewBox="0 0 100 100" fill="none" stroke="#222" stroke-width="3"><circle cx="14" cy="10" r="6"/><path d="M4 28c0-8 4-12 10-12s10 4 10 12"/><circle cx="86" cy="10" r="6"/><path d="M76 28c0-8 4-12 10-12s10 4 10 12"/><circle cx="14" cy="70" r="6"/><path d="M4 88c0-8 4-12 10-12s10 4 10 12"/><circle cx="86" cy="70" r="6"/><path d="M76 88c0-8 4-12 10-12s10 4 10 12"/><circle cx="50" cy="36" r="8"/><path d="M38 96V56h24v40M50 56v40"/><path d="M26 34l12 10M74 34l-12 10" stroke="var(--red)"/></svg>
  <h3>Vendors</h3><p>Nemo enim ipsam volup tatem quia ptsit.</p>
</div>
<div class="why" style="left:620px;top:3616px">
  <svg width="90" height="90" viewBox="0 0 90 90" fill="none" stroke-width="4"><rect x="4" y="4" width="72" height="72" stroke="#222"/><rect x="20" y="20" width="60" height="60" stroke="var(--red)" stroke-dasharray="8 6"/></svg>
  <h3>Transparent</h3><p>Nemo enim ipsam volup tatem quia ptsit.</p>
</div>

<!-- CONTACT FORM -->
<svg class="abs form-bg" width="1200" height="890" viewBox="0 0 1200 890" role="img" aria-label="Dark photo of an empty theater with rows of seats">
  <defs><linearGradient id="formFill" x1="0" y1="0" x2="0" y2="1"><stop offset="0" stop-color="#0d0a08"/><stop offset=".35" stop-color="#5a3d18"/><stop offset=".7" stop-color="#3a2810"/><stop offset="1" stop-color="#141010"/></linearGradient></defs>
  <polygon points="0,92 600,0 1200,92 1200,890 0,890" fill="url(#formFill)"/>
</svg>
<h2 class="h2 form-title">Send us a message</h2>
<span class="field-label" style="left:148px;top:3998px">Full name *</span>
<span class="field-label" style="left:454px;top:3998px">Email *</span>
<span class="field-label" style="left:758px;top:3998px">Phone *</span>
<span class="input" style="left:148px;top:4022px;width:292px"></span>
<span class="input" style="left:454px;top:4022px;width:292px"></span>
<span class="input" style="left:758px;top:4022px;width:294px"></span>
<span class="field-label" style="left:148px;top:4102px">Type of event *</span>
<span class="input" style="left:148px;top:4128px;width:904px"></span>
<span class="field-label" style="left:148px;top:4208px">Venue(s) of interest *</span>
<span class="check" style="left:150px;top:4250px"><i></i>Harlem</span>
<span class="check" style="left:258px;top:4250px"><i></i>Brooklyn</span>
<span class="check" style="left:378px;top:4250px"><i></i>Kindly Ashgrove</span>
<span class="check" style="left:528px;top:4250px"><i></i>Kindly Upper Ashgrove</span>
<span class="check" style="left:716px;top:4250px"><i></i>Kindly Fernwick</span>
<span class="check" style="left:150px;top:4284px"><i></i>Kindly Holloway (1)</span>
<span class="check" style="left:334px;top:4284px"><i></i>Kindly holloway (2)</span>
<span class="check" style="left:526px;top:4284px"><i></i>Kindly Holloway rooftop</span>
<span class="field-label" style="left:148px;top:4330px">Message *</span>
<span class="input" style="left:148px;top:4360px;width:904px;height:96px"></span>
<span class="abs btn submit">Submit</span>

<!-- FOOTER -->
<footer>
  <p class="abs foot-brand">KINDLYHOST</p>
  <p class="foot-item" style="top:4806px;width:300px"><svg width="12" height="16" viewBox="0 0 12 16"><path d="M6 0a6 6 0 0 1 6 6c0 4-6 10-6 10S0 10 0 6a6 6 0 0 1 6-6z" fill="var(--red)"/><circle cx="6" cy="6" r="2" fill="#fff"/></svg><span>Nemo enim ipsam voluptatem quia voluptas sit aspernatur.</span></p>
  <p class="foot-item" style="top:4862px"><svg width="14" height="14" viewBox="0 0 14 14"><path d="M3 0l3 3-2 2c1 2 3 4 5 5l2-2 3 3-2 3C6 14 0 8 0 2z" fill="var(--red)"/></svg><span>1 555 010 0199</span></p>
  <p class="foot-item" style="top:4908px"><svg width="15" height="12" viewBox="0 0 15 12"><rect width="15" height="12" rx="1" fill="var(--red)"/><path d="M1 2l6.5 5L14 2" stroke="#fff" fill="none"/></svg><span>info@kindlyhost.com</span></p>
  <div class="abs quick"><h4>Quick Links</h4><a>Location</a><a>FAQ</a><a>Contact</a></div>
  <div class="thumb" style="left:662px;top:4718px;background:linear-gradient(180deg,#7a4a2a,#3c4a44)" role="img" aria-label="Theater seating photo"></div>
  <div class="thumb" style="left:808px;top:4718px;background:linear-gradient(180deg,#e8e8ea,#6c6c78)" role="img" aria-label="Conference hall photo"></div>
  <div class="thumb" style="left:953px;top:4718px;background:linear-gradient(180deg,#2a1a18,#b03028)" role="img" aria-label="Cinema with red seats photo"></div>
  <div class="thumb" style="left:662px;top:4832px;background:linear-gradient(180deg,#2a3a8a,#5a6ac0)" role="img" aria-label="Blue-lit auditorium photo"></div>
  <div class="thumb" style="left:808px;top:4832px;background:linear-gradient(180deg,#f2f2f0,#9a9a9a)" role="img" aria-label="Banquet tables photo"></div>
  <div class="thumb" style="left:953px;top:4832px;background:linear-gradient(180deg,#a87a4a,#3a2412)" role="img" aria-label="Lecture hall photo"></div>
  <div class="thumb" style="left:662px;top:4946px;background:linear-gradient(180deg,#6a2aa0,#e04a3a)" role="img" aria-label="Concert crowd with stage lights photo"></div>
  <div class="thumb" style="left:808px;top:4946px;background:linear-gradient(180deg,#d06a3a,#8a3a1a)" role="img" aria-label="Orange-lit stage photo"></div>
  <div class="thumb" style="left:953px;top:4946px;background:linear-gradient(180deg,#c8d4ea,#b04a6a)" role="img" aria-label="Exhibition hall photo"></div>
  <div class="abs rule"></div>
  <p class="abs copy">Copyright © 2021, Kindlyhost. All rights reserved.</p>
  <div class="abs foot-socials"><span class="social" aria-label="Social link"></span><span class="social" aria-label="Social link"></span><span class="social" aria-label="Social link"></span></div>
</footer>

</body>
</html>
```